Develop new wine label for entry level Greek wines **

We need a label design for the new line of entry level Greek wines.

We will have 4 SKU: red dry wine, red semi sweet wine, white dry wine, white semi-sweet wines.

We would like to see traditional greek houses on it.

There needs to be a slight colour difference between dry and semi sweet wines (you can maybe change colours of some details in order to differentiate wines on the shelf).

We would like to use designs that use white and blue colours (I attached some images for your inspiration). The glass bottle will be transparent so keep in mind how the label will coordinate with the colour of the wine itself.

The label needs to communicate that the wine is from Greece, this wine is simple, approachable, easy to drink, modern and fun.

The brand name is the ancient Greek word "kelvo". Quoting knowlark: " Kelvo (ancient Greek: κἐλβος, plural: κἐλβοι; English prefix: eco- for ecology and economics) refers to three related but distinct concepts: the family, the family's property, and the house.".

So feel free to further elaborate on the concept.

The text that should appear on the label:
1. Brand name - Kelvo (a good idea would be to use a greek style shrift would be great to mimic greek letters κέλβος).
2. White semi-sweet / White dry / Red semi-sweet / Red dry

Target Market(s)

Ukraine

Font styles to use
Serif

Colors
33a6d7
cee9f5
ffffff
e34297

Requirements
Must have
• The customer needs to look at the bottle and understand that is it from Greece straight away.

```html
<!DOCTYPE html>
<html lang="en">
<head>
<meta charset="utf-8">
<title>Kelvo – Red Semi-Sweet Label</title>
<link rel="stylesheet" href="https://fonts.googleapis.com/css2?family=Cinzel:wght@500;600&family=Cormorant+Garamond:wght@600&display=swap">
<style>
  :root {
    --aegean: #33a6d7;
    --aegean-deep: #1f7fb3;
    --sky-pale: #cee9f5;
    --white: #ffffff;
    --label-ground: #fbfdfe;
    --wall: #eef3f6;
    --stone: #c9d3d8;
  }
  * { margin: 0; padding: 0; box-sizing: border-box; }
  html, body {
    width: 774px;
    height: 1200px;
    overflow: hidden;
    background: var(--white);
  }
  .label {
    position: relative;
    width: 774px;
    height: 1200px;
    background: var(--label-ground);
    overflow: hidden;
  }
  .label__top-band {
    position: absolute;
    left: 0; top: 0;
    width: 100%;
    height: 22px;
    background: var(--aegean);
  }
  .label__top-rule {
    position: absolute;
    left: 0; top: 30px;
    width: 100%;
    height: 3px;
    background: var(--aegean);
  }
  .brand {
    position: absolute;
    left: 0; top: 88px;
    width: 100%;
    text-align: center;
    font-family: "Cinzel", serif;
    font-weight: 600;
    font-size: 168px;
    line-height: 1;
    letter-spacing: 4px;
    color: var(--aegean);
  }
  .variety {
    position: absolute;
    left: 0; top: 286px;
    width: 100%;
    text-align: center;
    font-family: "Cormorant Garamond", serif;
    font-weight: 600;
    font-size: 30px;
    letter-spacing: 9px;
    color: var(--aegean-deep);
    text-transform: uppercase;
  }
  .scene {
    position: absolute;
    left: 0; top: 350px;
    width: 100%;
    height: 700px;
    background:
      radial-gradient(ellipse 60% 30% at 30% 30%, rgba(255,255,255,0.85), rgba(255,255,255,0) 70%),
      radial-gradient(ellipse 50% 25% at 75% 45%, rgba(255,255,255,0.7), rgba(255,255,255,0) 70%),
      linear-gradient(180deg, #4aa3d6 0%, #8cc7e6 35%, var(--sky-pale) 55%, var(--wall) 72%, var(--stone) 100%);
  }
  .label__bottom-rule {
    position: absolute;
    left: 0; top: 1062px;
    width: 100%;
    height: 3px;
    background: var(--aegean);
  }
  .volume {
    position: absolute;
    left: 0; top: 1090px;
    width: 100%;
    text-align: center;
    font-family: "Cormorant Garamond", serif;
    font-weight: 600;
    font-size: 40px;
    letter-spacing: 2px;
    color: var(--aegean-deep);
  }
  .label__bottom-band {
    position: absolute;
    left: 0; bottom: 0;
    width: 100%;
    height: 40px;
    background: var(--aegean);
  }
</style>
</head>
<body>
  <main class="label">
    <div class="label__top-band"></div>
    <div class="label__top-rule"></div>

    <h1 class="brand">KELVO</h1>
    <p class="variety">Red Semi-Sweet</p>

    <div class="scene" role="img" aria-label="Whitewashed Greek island houses with blue domed churches under a bright blue sky with soft white clouds"></div>

    <div class="label__bottom-rule"></div>
    <p class="volume">750ml</p>
    <div class="label__bottom-band"></div>
  </main>
</body>
</html>
```